Bref créative
Brightpath Outcomes Inc
I need double sided standard sized Business Card [3.5" x 2"]
You decid
Professional
Danielle Hartwell
CEO
4172 Juniper Ridge Drive,
Suite 517
Cedar Hollow, MN 48109
danielle.hartwell@brightpathoutcomes.example
www.brightpathoutcomes.example
On the back of the card we want another web adrdress of
walkingherownroute.example

```html
<!DOCTYPE html>
<html lang="en">
<head>
<meta charset="utf-8">
<title>Brightpath Outcomes Inc — Business Card</title>
<link rel="stylesheet" href="https://fonts.googleapis.com/css2?family=Arimo:wght@400;700&display=swap">
<style>
  :root {
    --page: #ffffff;
    --card-red: #ee3a3a;
    --card-red-deep: #d9262b;
    --card-red-soft: #f6686a;
    --card-charcoal: #3b3b3d;
    --ink-white: #ffffff;
    --ink-light: #d9d9d9;
    --accent-red: #ec2f33;
  }
  * { margin: 0; padding: 0; box-sizing: border-box; }
  html, body {
    width: 1200px;
    height: 1057px;
    overflow: hidden;
    background: var(--page);
    font-family: "Arimo", Arial, sans-serif;
  }
  .canvas { position: relative; width: 1200px; height: 1057px; }

  .card {
    position: absolute;
    left: 330px;
    width: 870px;
    height: 497px;
    overflow: hidden;
  }

  /* Back side */
  .card-back { top: 0; background: var(--card-red); }
  .card-back .profile-art {
    position: absolute;
    left: 0; top: 0;
    width: 100%; height: 100%;
    background: linear-gradient(100deg, var(--card-red) 0%, var(--card-red-soft) 45%, var(--card-red) 60%, var(--card-red-deep) 100%);
  }
  .card-back .back-url {
    position: absolute;
    right: 26px; top: 24px;
    color: var(--ink-white);
    font-weight: 700;
    font-size: 27px;
  }

  /* Front side */
  .card-front { top: 557px; background: var(--card-charcoal); color: var(--ink-white); }
  .front-url {
    position: absolute;
    right: 26px; top: 30px;
    font-weight: 700;
    font-size: 18px;
  }
  .brand {
    position: absolute;
    left: 36px; top: 130px;
    display: flex; align-items: center; gap: 18px;
  }
  .brand-mark {
    width: 58px; height: 58px;
    background: var(--accent-red);
  }
  .brand-text { display: flex; flex-direction: column; gap: 8px; }
  .brand-name {
    font-weight: 700;
    font-size: 34px;
    text-transform: uppercase;
    color: var(--ink-white);
    letter-spacing: 0.5px;
  }
  .brand-tagline {
    font-size: 15px;
    font-style: italic;
    color: var(--ink-light);
  }
  .contact {
    position: absolute;
    left: 36px; top: 320px;
    font-size: 20px;
    line-height: 25px;
  }
  .contact .address { margin-top: 18px; }
  .contact .email { margin-top: 22px; }
  .holder {
    position: absolute;
    right: 30px; top: 378px;
    text-align: right;
  }
  .holder-name {
    font-weight: 700;
    font-size: 42px;
    color: var(--accent-red);
  }
  .holder-title {
    font-size: 32px;
    color: var(--ink-white);
    margin-top: 2px;
  }
</style>
</head>
<body>
<main class="canvas">
  <section class="card card-back">
    <div class="profile-art" role="img" aria-label="Red pattern of layered side profiles facing each other"></div>
    <p class="back-url">www.walkingherownroute.example</p>
  </section>

  <section class="card card-front">
    <p class="front-url">www.brightpathoutcomes.example</p>
    <div class="brand">
      <div class="brand-mark"></div>
      <div class="brand-text">
        <span class="brand-name">Brightpath Outcomes Inc</span>
        <span class="brand-tagline">“Building a bolder you for every new stage”</span>
      </div>
    </div>
    <div class="contact">
      <p>Ph:&nbsp;&nbsp;&nbsp;612 555.0147</p>
      <p>Fax: 877.555.0182</p>
      <p class="address">4172 Juniper Ridge Drive,<br>Suite 517 Cedar Hollow, MN 48109</p>
      <p class="email">danielle.hartwell@brightpathoutcomes.example</p>
    </div>
    <div class="holder">
      <p class="holder-name">Danielle Hartwell</p>
      <p class="holder-title">CEO</p>
    </div>
  </section>
</main>
</body>
</html>
```